Brochure Design Project

We need a nice, warm, friendly Brochure for First Home Buyer in Australia.
It is actually a 32 pages Handbook. It has the Guide, what to aware and the process for first time home buyer.
Content will be provided.
And wish to have a flow with our letter head design or flyer design attached.
Reason: I need to show a example
Reason: We are waiting for more designers' submission.
Target Market(s)
First Home Buyer
Look and feel

```html
<!DOCTYPE html>
<html lang="en">
<head>
<meta charset="utf-8">
<title>First Home Buyer Handbook – Contents</title>
<link href="https://fonts.googleapis.com/css2?family=Arimo:wght@400;700&display=swap" rel="stylesheet">
<style>
  :root {
    --lime: #86d614;
    --lime-bright: #9be21f;
    --lime-pale: #d4f38c;
    --ink: #1a1a1a;
    --shadow: #1f1f1f;
    --paper: #ffffff;
    --box-tan: #c9a271;
    --box-light: #e2c9a2;
  }
  * { box-sizing: border-box; margin: 0; padding: 0; }
  html, body { width: 849px; height: 1200px; overflow: hidden; background: var(--paper); }
  body { font-family: "Arimo", Arial, sans-serif; color: var(--ink); }
  .page { position: relative; width: 849px; height: 1200px; overflow: hidden; background: var(--paper); }

  .wave { position: absolute; left: 0; width: 849px; }
  .wave--top { top: 0; height: 60px; }
  .wave--bottom { bottom: 0; height: 100px; }

  .brand { position: absolute; left: 700px; top: 110px; width: 130px; text-align: center; }
  .brand__mark { display: block; width: 30px; height: 30px; margin: 0 auto 8px; background: var(--lime); }
  .brand__name { font-size: 12px; font-weight: 700; color: #3e7d10; letter-spacing: 0.3px; }

  .section-title {
    position: absolute; left: 78px; height: 42px;
    background: var(--lime-bright);
    color: #fff; font-weight: 700; font-size: 20px;
    line-height: 42px; padding-left: 18px;
    box-shadow: 9px 6px 0 var(--shadow);
  }

  .toc { position: absolute; list-style: none; font-size: 17.5px; line-height: 25px; }
  .toc__item { display: flex; align-items: baseline; white-space: nowrap; }
  .toc__leader { flex: 1; overflow: hidden; margin: 0 1px; }
  .toc__leader::after { content: "........................................................................................................................................"; letter-spacing: 1px; }
  .toc--after { font-size: 18.5px; line-height: 27px; }

  .illustration-box {
    position: absolute; left: 0; top: 913px; width: 226px; height: 220px;
    background: linear-gradient(160deg, var(--box-light), var(--box-tan));
  }

  .disclaimer {
    position: absolute; left: 226px; top: 974px; width: 575px;
    font-size: 11.2px; line-height: 14.2px; text-align: justify;
  }
  .page-number { position: absolute; left: 778px; top: 1110px; font-size: 20px; font-weight: 700; }
</style>
</head>
<body>
<main class="page">
  <svg class="wave wave--top" viewBox="0 0 849 60" preserveAspectRatio="none" aria-hidden="true">
    <path d="M0 0H849V30C700 60 560 10 420 28C280 46 140 14 0 40Z" fill="var(--lime-pale)"/>
    <path d="M0 0H849V14C690 42 520 4 380 20C240 36 120 8 0 26Z" fill="var(--lime)"/>
  </svg>

  <div class="brand">
    <span class="brand__mark"></span>
    <span class="brand__name">Harbour Home Loans</span>
  </div>

  <h2 class="section-title" style="top:113px;width:283px;">Upfront Considerations</h2>
  <ul class="toc" style="left:149px;top:177px;width:582px;">
    <li class="toc__item">Budget plan<span class="toc__leader"></span>1</li>
    <li class="toc__item">Borrow capacity<span class="toc__leader"></span>1</li>
    <li class="toc__item">Required deposit<span class="toc__leader"></span>1</li>
    <li class="toc__item">First home owner grant<span class="toc__leader"></span>2</li>
    <li class="toc__item">First home saver account<span class="toc__leader"></span>5</li>
    <li class="toc__item">Which comes first, finance or property<span class="toc__leader"></span>6</li>
  </ul>

  <h2 class="section-title" style="top:341px;width:446px;">Considerations When Obtaining Finance</h2>
  <ul class="toc" style="left:149px;top:403px;width:546px;">
    <li class="toc__item">Choosing a mortgage broker<span class="toc__leader"></span>8</li>
    <li class="toc__item">Loan types<span class="toc__leader"></span>10</li>
    <li class="toc__item">Loan features<span class="toc__leader"></span>17</li>
    <li class="toc__item">Commonly used accounts<span class="toc__leader"></span>19</li>
    <li class="toc__item">Documents required<span class="toc__leader"></span>21</li>
  </ul>

  <h2 class="section-title" style="top:550px;width:488px;">Considerations When Purchasing A Property</h2>
  <ul class="toc" style="left:149px;top:613px;width:546px;">
    <li class="toc__item">Associated costs<span class="toc__leader"></span>22</li>
    <li class="toc__item">Home inspection<span class="toc__leader"></span>24</li>
    <li class="toc__item">Loan process<span class="toc__leader"></span>25</li>
    <li class="toc__item">Understand a contract of sale<span class="toc__leader"></span>26</li>
    <li class="toc__item">The general buying process<span class="toc__leader"></span>28</li>
    <li class="toc__item">The 7 mistakes first home buyers can avoid<span class="toc__leader"></span>30</li>
  </ul>

  <h2 class="section-title" style="top:784px;width:372px;">Considerations After Settlement</h2>
  <ul class="toc toc--after" style="left:139px;top:848px;width:570px;">
    <li class="toc__item">Moving<span class="toc__leader"></span>31</li>
    <li class="toc__item">How to pay off the mortgage<span class="toc__leader"></span>32</li>
  </ul>

  <div class="illustration-box" role="img" aria-label="Open cardboard moving box with a green recycling symbol on its side"></div>

  <svg class="wave wave--bottom" viewBox="0 0 849 100" preserveAspectRatio="none" aria-hidden="true">
    <path d="M0 70C160 30 330 90 500 60C650 34 760 40 849 20V100H0Z" fill="var(--lime-pale)"/>
    <path d="M0 88C180 60 340 100 520 78C670 60 770 62 849 48V100H0Z" fill="var(--lime)"/>
  </svg>

  <p class="disclaimer">Any comments and statements that are published herein are directly from the editorial contributors and should not be treated as a recommendation that a particular course of action is suitable for you. The opinions that have been expressed do not necessarily represent the viewpoints of the publisher and your use of any materials contained in this booklet is exclusively at your own risk. Although Harbour has taken all reasonable efforts and care to ensure that the information is correct at the time of publication, the accuracy and reliability of the published information cannot be guaranteed. Hence, Harbour will not assume any responsibility for the accuracy, completeness or authenticity of any published information and is not liable to you or any third party for any losses or damages suffered directly or indirectly through your use of the information. Copyright Harbour Finance and Property 2010</p>

  <span class="page-number">1</span>
</main>
</body>
</html>
```